黒の背景にムキムキの男性といったテイストではなく、清潔感のある優しいイメージでお願いいたします。
(イメージの参考)http://www.yukiura-dental.net/
表の面には陸上、サッカー、野球などのメジャースポーツの選手の写真を掲載して下さい。
【表面】・キャッチコピー・リード文・こんな方におすすめ・お客様の声
【裏面】・キャッチコピー・各商品の特徴・栄養士のプロフィール・料金プラン・申込の流れ
※詳細は添付ファイルをご確認下さいませ。
A4
両面
白を背景に、メインカラーはロゴと同じエメラルドグリーンでお願いいたします。
• 高解像度JPG (.jpg)
• イラストレーター形式 (.ai)
添付の写真素材もご利用下さいませ。
あまり時間もありませんので選定確約にいたします。
プロテインの価格は6,980円(税抜)に変更をお願いいたします。
プロテインの写真を撮り直しました。こちらをご利用下さいませ。
「私がサポートします!」のところの文章につきまして、「ジムストラクターも兼務」とありますが、正しくは「ジムインストラクターも兼務」でございます。申し訳ございませんがよろしくお願い致します。
また、プロテインはパッケージと出来上がりの写真と両方を掲載して頂けますと幸いです。どうぞよろしくお願い致します。
裏面の情報が少し多いと思いましたので、「私がサポートします!」などの部分は必要に応じて表面にレイアウトしてご提案頂いて結構でございます。何卒よろしくお願い致します。
「青嶺集成」Vol.71(http://www.seireishusei.com/cdrom/seireishusei.asp?vol=71)の素材は持っていますので、こちらの素材を使って頂いても結構です。仮で当て込んで頂ければ選定した際に該当する写真をお渡しいたします。外人さんはイメージと違いますのでお控え下さいませ。
栄養カウンセリングの価格が1,980円になっておりますが、正しくは1,750円(税抜)になります。申し訳ございませんがよろしくお願い致します。

全体的にスッキリしていて、雰囲気の優しい感じがイメージにぴったりでした。

ご提案頂きました皆様、ありがとうございました。どれもいいデザインで、選定はとても悩みました。
当選しなかった方には大変申し訳ございませんが、機会がございましたらまたお力添え頂けますと幸いです。

```html
<!DOCTYPE html>
<html lang="ja">
<head>
<meta charset="utf-8">
<title>アクアリート 栄養サポート</title>
<link href="https://fonts.googleapis.com/css2?family=Noto+Sans+JP:wght@400;500;700;900&family=Montserrat:ital,wght@0,600;0,800;1,700&display=swap" rel="stylesheet">
<style>
:root{
  --green:#1bb195;
  --green-dark:#0f8f78;
  --green-pale:#e2f4ef;
  --ink:#333;
  --muted:#666;
  --white:#fff;
}
*{margin:0;padding:0;box-sizing:border-box}
html,body{width:855px;height:1200px;overflow:hidden;background:var(--white)}
body{font-family:"Noto Sans JP",sans-serif;color:var(--ink);position:relative}
.abs{position:absolute}
.kicker{left:28px;top:16px;font-size:21px;font-weight:700;color:var(--green);font-style:italic;letter-spacing:2px}
.headline{left:26px;top:48px;font-size:46px;line-height:1.0;font-weight:900;color:var(--green);letter-spacing:0}
.headline span{display:block;margin-bottom:6px}
.photo{position:absolute;border-radius:50%;border:4px solid var(--white)}
.p-tennis{left:615px;top:6px;width:195px;height:195px;background:radial-gradient(circle at 40% 40%,#8ec9e8,#3b7fa8 70%,#2d5f3a)}
.p-runners{left:0;top:152px;width:195px;height:165px;border-radius:0 50% 50% 0;background:linear-gradient(150deg,#c9b8a1,#7c5a3e 60%,#a4432e)}
.p-sprint{left:14px;top:330px;width:105px;height:95px;background:linear-gradient(160deg,#d9c7ad,#9a6b43 70%,#5b6f8d)}
.p-soccer{left:196px;top:150px;width:300px;height:300px;background:radial-gradient(circle at 50% 35%,#5c8fc0,#2c5f8d 45%,#3f8a3e 75%,#2b6a2e)}
.p-baseball{left:470px;top:215px;width:135px;height:135px;background:linear-gradient(170deg,#b9c8b2,#6e8e5c 55%,#d9d2c4)}
.p-bike-s{left:440px;top:365px;width:90px;height:90px;background:linear-gradient(150deg,#9fb4c4,#4e6070 60%,#c95a3a)}
.p-bike-r{left:695px;top:190px;width:165px;height:190px;border-radius:50% 0 0 50%;background:linear-gradient(170deg,#a8c4d4,#5a7383 55%,#2f3b44)}
.brand{left:590px;top:392px;width:200px;height:40px;display:flex;align-items:center;justify-content:center;gap:8px}
.brand-dot{width:16px;height:16px;border-radius:50%;background:var(--green)}
.brand-name{font-family:"Montserrat",sans-serif;font-weight:800;font-size:22px;color:var(--green);letter-spacing:1px}
.lead{left:28px;top:470px;width:400px;font-size:11.5px;line-height:1.85;color:var(--ink)}
.recommend{left:456px;top:462px;width:370px}
.recommend h2{font-size:19px;font-weight:700;color:var(--green);text-align:center;margin-bottom:8px}
.recommend li{list-style:none;font-size:14px;font-weight:700;padding:3px 0 4px 26px;border-bottom:2px solid var(--green);margin-bottom:6px;position:relative}
.recommend li::before{content:"";position:absolute;left:4px;top:8px;width:12px;height:12px;background:var(--green);border-radius:2px}
.features-title{left:0;top:660px;width:855px;text-align:center;font-size:20px;font-weight:700;color:var(--green);letter-spacing:3px}
.features-band{left:0;top:694px;width:855px;height:192px;background:var(--green-pale)}
.features{left:32px;top:706px;width:792px;display:flex;gap:14px}
.card{flex:1;height:168px;background:var(--white);border:2px solid var(--green);border-radius:4px;text-align:center;padding:8px 4px 0}
.card p{font-size:12.5px;font-weight:700;line-height:1.4;height:72px;display:flex;align-items:center;justify-content:center}
.card svg{display:block;margin:4px auto 2px}
.card em{font-family:"Montserrat",sans-serif;font-style:italic;font-weight:700;font-size:13px;color:var(--green)}
.section-h{font-size:21px;font-weight:900;color:var(--green)}
.supporter{left:28px;top:900px;width:350px}
.s-photo{position:absolute;left:0;top:38px;width:128px;height:116px;background:linear-gradient(180deg,#e9eef1,#c7d2da 60%,#f4f4f4)}
.s-name{position:absolute;left:140px;top:36px;font-size:10px;color:var(--muted)}
.s-name b{display:block;font-size:17px;color:var(--ink);margin-top:2px}
.s-name small{display:block;font-family:"Montserrat",sans-serif;font-size:8px;color:var(--green);letter-spacing:1px}
.s-text{position:absolute;left:140px;top:96px;width:210px;font-size:10px;line-height:1.75}
.s-sub{position:absolute;left:0;top:162px;width:130px;font-size:9px;line-height:1.6;color:var(--muted)}
.voice{left:398px;top:900px;width:430px;height:205px;border:2px solid var(--green);border-radius:4px}
.voice-bar{position:absolute;left:-2px;top:-2px;width:430px;height:26px;background:var(--green);color:var(--white);font-size:14px;font-weight:700;padding:3px 0 0 12px}
.voice-bar i{font-family:"Montserrat",sans-serif;font-size:10px;margin-left:6px;opacity:.9}
.v-photo{position:absolute;left:12px;top:38px;width:168px;height:152px;background:linear-gradient(165deg,#bcd3c2,#7a9b80 50%,#3e4f48)}
.v-head{position:absolute;left:192px;top:34px;width:226px;font-size:15px;font-weight:900;line-height:1.4;color:var(--green-dark)}
.v-text{position:absolute;left:192px;top:82px;width:226px;font-size:10px;line-height:1.75}
</style>
</head>
<body>
<p class="abs kicker">スポーツ栄養士がサポート！</p>
<h1 class="abs headline"><span>自分専用の栄養で</span><span>最高のパフォーマンスに!</span></h1>

<div class="photo p-tennis" role="img" aria-label="テニス選手がボールを打つ写真"></div>
<div class="photo p-bike-r" role="img" aria-label="ロードバイクで走る選手の写真"></div>
<div class="photo p-runners" role="img" aria-label="陸上選手がハードルを走る写真"></div>
<div class="photo p-sprint" role="img" aria-label="短距離走のスタート場面の写真"></div>
<div class="photo p-baseball" role="img" aria-label="野球選手が投球する写真"></div>
<div class="photo p-soccer" role="img" aria-label="サッカー選手がボールを蹴る写真"></div>
<div class="photo p-bike-s" role="img" aria-label="自転車競技の選手の写真"></div>

<div class="abs brand"><span class="brand-dot"></span><span class="brand-name">AQUALETE</span></div>

<p class="abs lead">自分はどれくらいの栄養が必要なのか、ご存知ですか？必要な栄養は一人ひとり異なり、またその人の競技によっても異なります。食事の質は力を出すために欠かせないものです。毎日の食事を見直すことで、体の動きや回復力が変わります。私たちは一人ひとりの体と目標に合わせた栄養を提案し、結果につながる体づくりをサポートします。試合で力を出したいアスリートを、スポーツ栄養士がマンツーマンでサポートします。</p>

<section class="abs recommend">
  <h2>こんな方におすすめ!</h2>
  <ul>
    <li>後半に競り勝つスタミナをつけたい</li>
    <li>試合で100%のパフォーマンスを出したい</li>
    <li>筋肉を落とさずに減量したい</li>
    <li>当たり負けしない強い体を作りたい</li>
  </ul>
</section>

<h2 class="abs features-title">アクアリートの栄養サポートの特徴</h2>
<div class="abs features-band"></div>
<div class="abs features">
  <div class="card"><p>スポーツ<br>栄養士の<br>マンツーマン指導</p>
    <svg width="70" height="52" viewBox="0 0 70 52"><rect x="4" y="6" width="34" height="24" rx="5" fill="var(--green)"/><path d="M12 30 l-2 10 l10-10z" fill="var(--green)"/><rect x="30" y="18" width="34" height="24" rx="5" fill="none" stroke="var(--green)" stroke-width="3"/></svg>
    <em>one-on-one</em></div>
  <div class="card"><p>メールカウンセリング<br>だから忙しくても<br>手軽に相談できる</p>
    <svg width="70" height="52" viewBox="0 0 70 52"><rect x="8" y="8" width="54" height="36" rx="3" fill="var(--green)"/><path d="M8 10 L35 30 L62 10" fill="none" stroke="#fff" stroke-width="3"/></svg>
    <em>mail counseling</em></div>
  <div class="card"><p>一人ひとりに<br>合わせた<br>オーダーメイドの<br>サプリメント</p>
    <svg width="70" height="52" viewBox="0 0 70 52"><rect x="10" y="4" width="50" height="34" rx="3" fill="var(--green)"/><rect x="15" y="9" width="40" height="24" fill="#fff"/><rect x="30" y="38" width="10" height="7" fill="var(--green)"/><rect x="22" y="45" width="26" height="4" fill="var(--green)"/></svg>
    <em>custom-made</em></div>
  <div class="card"><p>高濃度で<br>飲みやすい<br>オリジナル<br>プロテイン</p>
    <svg width="70" height="52" viewBox="0 0 70 52"><rect x="26" y="2" width="18" height="8" fill="var(--green)"/><rect x="20" y="10" width="30" height="40" rx="5" fill="var(--green)"/><rect x="24" y="22" width="22" height="12" fill="#fff"/></svg>
    <em>original protein</em></div>
</div>

<section class="abs supporter">
  <h2 class="section-h">私がサポートします!</h2>
  <div class="s-photo" role="img" aria-label="スポーツ栄養士の人物写真"></div>
  <div class="s-name">スポーツ栄養士<b>高森 直樹</b><small>TAKAMORI NAOKI</small></div>
  <p class="s-text">管理栄養士の資格を取得後、スポーツ栄養の分野で多くのアスリートを指導。現在はジムインストラクターも兼務し、トレーニングと食事の両面から選手の体づくりを支えています。競技ごとの特性を理解した上で、一人ひとりに合わせたプランを提案します。</p>
  <p class="s-sub">管理栄養士／公認スポーツ栄養士<br>ジムインストラクター兼務</p>
</section>

<section class="abs voice">
  <div class="voice-bar">お客様の声<i>VOICE</i></div>
  <div class="v-photo" role="img" aria-label="ロードバイクに乗るお客様の写真"></div>
  <p class="v-head">300kmのレースの後でも<br>筋肉痛になりませんでした</p>
  <p class="v-text">長距離のレースの後はいつも体が重く、回復に時間がかかっていました。栄養士の方にアドバイスをもらい、食事とプロテインを見直したところ、レース後の疲れが驚くほど軽くなりました。今では練習の質も上がり、自己ベストを更新できています。</p>
</section>
</body>
</html>
```